cover for CD- Single.

This design is for a CD cover. The design is at your disposal, using all of your creative talents.
Things to improve the photo: Cleaning the face, removing blemishes.
Design in black and white would be an option (Color would be another option). I reiterate it is up to your taste and criteria, any reform and art on the cover of Cd.
Name of the single: El Camino del Alba Serena
Artist Name: Marisol Quenteva

Target Market(s)

Single Music

Industry/Entity Type

Music

Colors

Designer to choose colors to be used in the design.

Requirements
Must have
• style, elegance, professionalism, spontaneity
Nice to have
• I want it to be as professional as possible.
Should not have
• Spelling errors.

```html
<!DOCTYPE html>
<html lang="es">
<head>
<meta charset="utf-8">
<title>Marisol Quenteva – El Camino del Alba Serena</title>
<link rel="stylesheet" href="https://fonts.googleapis.com/css2?family=Playfair+Display:wght@400;600&family=Bodoni+Moda:wght@400&display=swap">
<style>
:root{
  --page:#ececec;
  --paper:#e9e9e9;
  --paper-inner:#cfcfcf;
  --tray:#f3f3f3;
  --disc:#ededed;
  --ink:#111;
  --band:#707070;
  --band-text:#f2f2f2;
  --photo-light:#f0f0f0;
  --photo-dark:#5a5a5a;
  --heart:#c4161c;
}
*{margin:0;padding:0;box-sizing:border-box}
html,body{width:1200px;height:2214px;overflow:hidden}
body{background:var(--page);position:relative;font-family:"Playfair Display",serif;color:var(--ink)}
.panel{position:absolute;background:var(--paper);overflow:hidden}
.artist{font-family:"Playfair Display",serif;font-weight:600;white-space:nowrap;text-align:center;position:absolute;left:0;right:0}
.title-stack{font-family:"Bodoni Moda",serif;font-weight:400;position:absolute}
.title-stack span{display:block}
.photo{position:absolute;background:linear-gradient(100deg,var(--photo-light) 0%,#c9c9c9 45%,var(--photo-dark) 100%)}
.heart{position:absolute;width:20px;height:20px}

/* front cover */
.front{left:357px;top:182px;width:498px;height:448px}
.front .artist{top:52px;font-size:30px}
.front .band{position:absolute;left:110px;top:145px;right:0;height:163px;background:var(--band)}
.front .band .photo{left:0;top:0;width:170px;height:163px;background:linear-gradient(90deg,var(--photo-light) 0%,#bdbdbd 60%,var(--band) 100%)}
.front .title-stack{left:333px;top:148px;font-size:29px;line-height:30.5px;color:var(--band-text)}
.front .heart{left:238px;top:374px}

/* back cover */
.back{left:365px;top:880px;width:496px;height:448px}
.back .artist{top:36px;font-size:27px}
.back .subtitle{position:absolute;left:0;right:0;top:78px;text-align:center;font-family:"Bodoni Moda",serif;font-size:25px;white-space:nowrap}
.back .photo{left:353px;top:135px;width:143px;height:190px;background:linear-gradient(90deg,var(--paper) 0%,#d2d2d2 45%,var(--photo-dark) 100%)}
.back .songs-head{position:absolute;left:105px;top:172px;font-family:"Bodoni Moda",serif;font-size:26px}
.tracklist{position:absolute;left:108px;top:224px;list-style:none;font-size:8px;line-height:14.5px}
.tracklist b{font-weight:400;display:inline-block;width:10px}
.back .heart{left:241px;top:397px;width:14px;height:14px}

/* inside spread */
.booklet{left:199px;top:1627px;width:391px;height:358px;background:var(--paper-inner)}
.booklet .title-stack{left:28px;top:100px;font-size:23px;line-height:26px}
.booklet .hello{position:absolute;left:111px;top:62px;font-size:14px;font-weight:600;letter-spacing:.5px}
.booklet .letter{position:absolute;left:111px;top:108px;width:238px;font-size:6px;line-height:11.5px}
.booklet .letter p{margin-bottom:11px}
.booklet .sign{position:absolute;left:0;right:0;top:294px;text-align:center;font-size:11px}
.booklet .heart{left:189px;top:314px;width:12px;height:12px}

.tray{left:603px;top:1630px;width:400px;height:352px;background:var(--tray);border:1px solid #dcdcdc}
.disc{position:absolute;left:35px;top:10px;width:336px;height:336px;border-radius:50%;background:var(--disc);overflow:hidden;border:3px solid #d8d8d8}
.disc .artist{top:52px;font-size:19px}
.disc .title-stack{left:52px;top:103px;font-size:22px;line-height:26px}
.disc .photo{left:209px;top:105px;width:150px;height:140px;background:linear-gradient(90deg,var(--disc) 0%,#c4c4c4 45%,var(--photo-dark) 100%)}
.disc .hub{position:absolute;left:141px;top:128px;width:66px;height:66px;border-radius:50%;background:#dedede;border:2px solid #cfcfcf}
.disc .hub::after{content:"";position:absolute;left:20px;top:20px;width:22px;height:22px;border-radius:50%;background:var(--tray)}
.disc .heart{left:158px;top:272px;width:18px;height:18px}
</style>
</head>
<body>

<svg width="0" height="0" style="position:absolute" aria-hidden="true">
  <symbol id="heart" viewBox="0 0 20 20">
    <path d="M10 18 C4 13 1 10 1 6 C1 3 3 1.5 5.5 1.5 C7.5 1.5 9 3 10 4.5 C11 3 12.5 1.5 14.5 1.5 C17 1.5 19 3 19 6 C19 10 16 13 10 18 Z" fill="var(--heart)"/>
  </symbol>
</svg>

<section class="panel front" aria-label="Portada">
  <h1 class="artist">Marisol Quenteva</h1>
  <div class="band">
    <div class="photo" role="img" aria-label="Retrato en blanco y negro de la artista"></div>
  </div>
  <h2 class="title-stack"><span>El</span><span>Camino</span><span>del</span><span>Alba</span><span>Serena</span></h2>
  <svg class="heart"><use href="#heart"/></svg>
</section>

<section class="panel back" aria-label="Contraportada">
  <div class="artist">Marisol Quenteva</div>
  <div class="subtitle">El Camino del Alba Serena</div>
  <div class="photo" role="img" aria-label="Retrato en blanco y negro de la artista"></div>
  <h3 class="songs-head">Canciones</h3>
  <ol class="tracklist">
    <li><b>1</b>Lorem ipsum dolor sit amet,</li>
    <li><b>2</b>Consectetur adipiscing elit, sed do eiusmod</li>
    <li><b>3</b>Magna aliqua. Quis ipsum suspendisse ultrices gravida.</li>
    <li><b>4</b>Consectetur adipiscing elit, sed do eiusmod</li>
    <li><b>5</b>Lorem ipsum dolor sit amet,</li>
  </ol>
  <svg class="heart"><use href="#heart"/></svg>
</section>

<section class="panel booklet" aria-label="Libreto interior">
  <div class="title-stack"><span>El</span><span>Camino</span><span>del</span><span>Alba</span><span>Serena</span></div>
  <div class="hello">HELLO</div>
  <div class="letter">
    <p>Estas canciones nacieron en noches largas y mañanas tranquilas, entre amigos, guitarras y silencios compartidos. Cada una guarda un pedazo del camino que me trajo hasta aquí.</p>
    <p>Gracias a mi familia por su paciencia y a quienes creyeron en esta música desde el primer día.</p>
    <p>Este disco es para ti, que escuchas con el corazón abierto. Que estas melodías te acompañen en cada amanecer y te recuerden que siempre hay una razón para cantar.</p>
  </div>
  <div class="sign">Marisol Quenteva</div>
  <svg class="heart"><use href="#heart"/></svg>
</section>

<section class="panel tray" aria-label="Disco">
  <div class="disc">
    <div class="artist">Marisol Quenteva</div>
    <div class="photo" role="img" aria-label="Retrato en blanco y negro de la artista"></div>
    <div class="title-stack"><span>El</span><span>Camino</span><span>del</span><span>Alba</span><span>Serena</span></div>
    <div class="hub"></div>
    <svg class="heart"><use href="#heart"/></svg>
  </div>
</section>

</body>
</html>
```